Terrace Anchoring Works business card

As per your previous logo design, I would like to incorporate all those colours into the card.
I've added a business card I don't mind which is double sided. Also my Po box number..
Could be in a format so I can add new email, ph numbers etc.

Thanks

• My logo that is attached and the same colour scheme

```html
<!DOCTYPE html>
<html lang="en">
<head>
<meta charset="utf-8">
<title>Terrace Anchoring Works – Business Card</title>
<link rel="stylesheet" href="https://fonts.googleapis.com/css2?family=Open+Sans:wght@400;600;700;800&display=swap">
<style>
  :root {
    --page: #e9e9ea;
    --card-dark: #141414;
    --card-mid: #2a2a2b;
    --divider: #8a8a8c;
    --brand-blue: #1a8fd6;
    --text-light: #e6e6e6;
    --text-soft: #cfcfcf;
  }
  * { box-sizing: border-box; margin: 0; padding: 0; }
  html, body { width: 1180px; height: 1200px; overflow: hidden; }
  body {
    background: var(--page);
    font-family: "Open Sans", Arial, sans-serif;
    position: relative;
  }
  .card-sheet {
    position: absolute;
    left: 0; top: 420px;
    width: 1180px;
    background: var(--divider);
  }
  .card-row {
    display: flex;
    justify-content: space-between;
    gap: 12px;
  }
  .card {
    position: relative;
    width: 584px;
    height: 330px;
    overflow: hidden;
  }
  .card-texture {
    position: absolute; inset: 0;
    background:
      radial-gradient(ellipse at 25% 30%, rgba(90,90,92,.55), transparent 55%),
      radial-gradient(ellipse at 80% 70%, rgba(70,70,72,.4), transparent 60%),
      linear-gradient(160deg, var(--card-mid), var(--card-dark));
  }
  .brand-band {
    height: 16px;
    background: var(--brand-blue);
  }
  .brand-name {
    position: absolute;
    display: flex;
    align-items: center;
    gap: 8px;
    color: var(--brand-blue);
    font-weight: 800;
    line-height: 1;
  }
  .brand-mark {
    width: 12px; height: 12px;
    background: var(--text-light);
  }
  .card-front .brand-name {
    left: 36px; top: 78px;
    font-size: 19px;
    width: 190px;
  }
  .card-back .brand-name {
    left: 50%; top: 50%;
    transform: translate(-50%, -50%);
    font-size: 34px;
    white-space: nowrap;
  }
  .contact-block {
    position: absolute;
    left: 253px; top: 48px;
    color: var(--text-light);
  }
  .person-name {
    color: var(--brand-blue);
    font-weight: 700;
    font-size: 16px;
    line-height: 1.1;
  }
  .person-role {
    font-size: 12px;
    color: var(--text-soft);
  }
  .company {
    margin-top: 30px;
    font-size: 14px;
    font-weight: 700;
    letter-spacing: .2px;
  }
  .company-short { color: var(--brand-blue); }
  .address {
    font-size: 13.5px;
    line-height: 19px;
    margin-top: 2px;
  }
  .contact-list {
    list-style: none;
    margin-top: 34px;
    font-size: 13.5px;
    line-height: 19px;
  }
  .contact-list li {
    display: flex;
    align-items: center;
    gap: 10px;
  }
  .contact-list .gap-before { margin-top: 6px; }
  .contact-icon {
    width: 13px; height: 13px;
    fill: var(--brand-blue);
    flex: none;
  }
</style>
</head>
<body>
  <section class="card-sheet">
    <div class="card-row">
      <article class="card card-front">
        <div class="card-texture" role="img" aria-label="Dark brushed-metal hexagon pattern background"></div>
        <div class="brand-name"><span class="brand-mark"></span>TAW</div>
        <div class="contact-block">
          <p class="person-name">Liam Corwell</p>
          <p class="person-role">Supervisor</p>
          <p class="company"><span class="company-short">TAW</span> TERRACE ANCHORING WORKS</p>
          <p class="address">PO Box 418<br>Maitland NSW&nbsp;&nbsp;2320</p>
          <ul class="contact-list">
            <li>
              <svg class="contact-icon" viewBox="0 0 16 16" aria-hidden="true"><path d="M2 6c0-2 2-3 6-3s6 1 6 3v1h-3V6H5v1H2z M4 8h8l1 5H3z"/></svg>
              0 412 550 317
            </li>
            <li>
              <svg class="contact-icon" viewBox="0 0 16 16" aria-hidden="true"><path d="M2 6c0-2 2-3 6-3s6 1 6 3v1h-3V6H5v1H2z M4 8h8l1 5H3z"/></svg>
              1 800 555 0199
            </li>
            <li class="gap-before">
              <svg class="contact-icon" viewBox="0 0 16 16" aria-hidden="true"><path d="M1 3h14v10H1z M2 4l6 5 6-5" fill="none" stroke="#1a8fd6" stroke-width="1.4"/><path d="M1 3h14L8 8z"/></svg>
              director@taworks.com.au
            </li>
            <li>
              <svg class="contact-icon" viewBox="0 0 16 16" aria-hidden="true"><path d="M1.5 2.5h13v9h-13z" fill="none" stroke="#1a8fd6" stroke-width="1.4"/><path d="M5 14h6v1H5z"/></svg>
              website if needed here
            </li>
          </ul>
        </div>
      </article>
      <article class="card card-back">
        <div class="card-texture" role="img" aria-label="Dark brushed-metal hexagon pattern background"></div>
        <div class="brand-name"><span class="brand-mark"></span>TERRACE ANCHORING WORKS</div>
      </article>
    </div>
    <div class="brand-band"></div>
  </section>
</body>
</html>
```